Water Filtration Company needs a business card design using our existing logo/colours!

We design and manufacture and export specialised water filtration equipment. Our equipment will take unclean dirty water and filters to safe clean drinkable water.
We would like to see designs using our existing logo and colours (see attached "Palette") that represents clean safe drinking water (fresh, clean designs but still professional and modern). Our customers are other businesses who supply water filtration equipment, governments, and private individuals.
BUSINESS CARD DETAILS (Common details):
Tel: + 61 7 55 419 276
www: brindlepeak.com.au
Address: 3/47 Cordwell Parade
Marlow Flats NSW 2593 Australia
(please include the word Australia as we are an international company)
Must include: COMMERCIAL WATER FILTRATION EQUIPMENT
NAME NO 1:
Owen Pritch
General Manager
Mobile: +61 427 38 91 04
Email: owen@brindlepeak.com.au
NAME NO. 2:
Gina Rosk
Business Manager
Mobile: +61 409 572 148
Email: gina@brindlepeak.com.au
Must Have:
1) PRINT READY IN .AI & .PDF FORMATS
2) Also saved in file format .ai (Adobe Illustrator - compatible with CS4)
3) Use existing LOGO & COLOURS: Please use our logo (see attached file)
4) FONTS: we have used Avenir & Helvetica in the past but are open to other font types for the address etc.
Thank you!

```html
<!DOCTYPE html>
<html lang="en">
<head>
<meta charset="utf-8">
<title>Brindle Peak business cards</title>
<link href="https://fonts.googleapis.com/css2?family=PT+Sans+Narrow:wght@400;700&family=Open+Sans:wght@700&display=swap" rel="stylesheet">
<style>
  :root {
    --ink: #0d4f7a;
    --brand: #1a82a8;
    --deep: #0a5a8a;
    --sky: #3fb7c9;
    --band-light: #b9e8f1;
    --band-mid: #23a4c2;
    --band-dark: #0b6890;
    --tag-dark: #0c3a55;
    --white: #ffffff;
    --crop: #555555;
  }
  * { box-sizing: border-box; margin: 0; padding: 0; }
  html, body { width: 1200px; height: 1168px; overflow: hidden; background: var(--white); }
  .sheet { position: relative; width: 1200px; height: 1168px; }

  .crop-v { position: absolute; width: 1px; background: var(--crop); }
  .crop-h { position: absolute; height: 1px; width: 22px; background: var(--crop); }

  .card { position: absolute; width: 548px; }
  .card-front { left: 40px; height: 357px; background: var(--white); }
  .card-back {
    left: 606px; height: 348px;
    background: linear-gradient(180deg, var(--sky) 0%, #1493b5 45%, var(--deep) 100%);
  }

  .wordmark {
    font-family: "PT Sans Narrow", sans-serif;
    font-weight: 700;
    letter-spacing: 0.01em;
    line-height: 1;
    display: flex; align-items: center; gap: 12px;
  }
  .wordmark .dot { width: 16px; height: 16px; border-radius: 50%; }
  .card-front .wordmark { position: absolute; left: 38px; top: 42px; font-size: 58px; color: var(--brand); }
  .card-front .wordmark .dot { background: var(--brand); }
  .card-back .wordmark { position: absolute; left: 0; right: 0; top: 124px; justify-content: center; font-size: 70px; color: var(--white); }
  .card-back .wordmark .dot { background: var(--white); width: 18px; height: 18px; }

  .contact {
    position: absolute; top: 204px;
    font-family: "PT Sans Narrow", sans-serif;
    font-size: 15px; line-height: 21.6px; color: var(--ink);
  }
  .contact-company { left: 38px; }
  .contact-person { right: 33px; text-align: right; }
  .contact-person .name, .contact-person .role { font-weight: 700; }

  .band {
    position: absolute; left: 0; right: 0; top: 300px; height: 57px;
    background: linear-gradient(180deg, var(--band-light) 0%, var(--band-mid) 45%, var(--band-dark) 100%);
  }
  .tagline {
    font-family: "Open Sans", sans-serif; font-weight: 700;
    font-size: 9.5px; letter-spacing: 0.42em; white-space: nowrap;
  }
  .band .tagline { position: absolute; left: 38px; top: 10px; color: var(--tag-dark); }
  .card-back .tagline { position: absolute; left: 0; right: 0; top: 310px; text-align: center; color: var(--white); }
</style>
</head>
<body>
<div class="sheet">
  <!-- crop marks -->
  <div class="crop-v" style="left:57px;top:60px;height:72px"></div>
  <div class="crop-v" style="left:574px;top:60px;height:72px"></div>
  <div class="crop-v" style="left:622px;top:60px;height:72px"></div>
  <div class="crop-v" style="left:57px;top:522px;height:72px"></div>
  <div class="crop-v" style="left:574px;top:522px;height:72px"></div>
  <div class="crop-v" style="left:622px;top:522px;height:72px"></div>
  <div class="crop-v" style="left:57px;top:632px;height:72px"></div>
  <div class="crop-v" style="left:574px;top:632px;height:72px"></div>
  <div class="crop-v" style="left:622px;top:632px;height:72px"></div>
  <div class="crop-v" style="left:57px;top:1092px;height:72px"></div>
  <div class="crop-v" style="left:574px;top:1092px;height:72px"></div>
  <div class="crop-v" style="left:622px;top:1092px;height:72px"></div>
  <div class="crop-h" style="left:0;top:168px"></div>
  <div class="crop-h" style="left:0;top:486px"></div>
  <div class="crop-h" style="left:0;top:740px"></div>
  <div class="crop-h" style="left:0;top:1056px"></div>
  <div class="crop-h" style="left:1178px;top:168px"></div>
  <div class="crop-h" style="left:1178px;top:486px"></div>
  <div class="crop-h" style="left:1178px;top:740px"></div>
  <div class="crop-h" style="left:1178px;top:1056px"></div>

  <!-- Owen Pritch -->
  <section class="card card-front" style="top:154px">
    <div class="wordmark"><span class="dot"></span>Brindle Peak</div>
    <div class="contact contact-company">
      <p>Tel: + 61 7 55 419 276</p>
      <p>www.brindlepeak.com.au</p>
      <p>3/47 Cordwell Parade</p>
      <p>Marlow Flats, NSW 2593, Australia</p>
    </div>
    <div class="contact contact-person">
      <p class="name">Owen Pritch</p>
      <p class="role">General Manager</p>
      <p>Mobile +61 427 38 91 04</p>
      <p>email owen@brindlepeak.com.au</p>
    </div>
    <div class="band"><p class="tagline">COMMERCIAL WATER FILTRATION EQUIPMENT</p></div>
  </section>
  <section class="card card-back" style="top:154px">
    <div class="wordmark"><span class="dot"></span>Brindle Peak</div>
    <p class="tagline">COMMERCIAL WATER FILTRATION EQUIPMENT</p>
  </section>

  <!-- Gina Rosk -->
  <section class="card card-front" style="top:724px">
    <div class="wordmark"><span class="dot"></span>Brindle Peak</div>
    <div class="contact contact-company">
      <p>Tel: + 61 7 55 419 276</p>
      <p>www.brindlepeak.com.au</p>
      <p>3/47 Cordwell Parade</p>
      <p>Marlow Flats, NSW 2593, Australia</p>
    </div>
    <div class="contact contact-person">
      <p class="name">Gina Rosk</p>
      <p class="role">Business Manager</p>
      <p>Mobile +61 409 572 148</p>
      <p>email gina@brindlepeak.com.au</p>
    </div>
    <div class="band"><p class="tagline">COMMERCIAL WATER FILTRATION EQUIPMENT</p></div>
  </section>
  <section class="card card-back" style="top:724px">
    <div class="wordmark"><span class="dot"></span>Brindle Peak</div>
    <p class="tagline">COMMERCIAL WATER FILTRATION EQUIPMENT</p>
  </section>
</div>
</body>
</html>
```